Design a Website for an IT Support Company

We are an IT support company that provides commercial IT support and services to small and medium sized businesses. We are in need of a website to be developed for our business.
We would like to work with someone who is either familiar with the IT field, or has developed a website for an IT support company in the past.
Some examples of designs/layouts that we like:
https://www.veltragrid.example/
http://www.morvashelp.example/
http://kelbo.example/
http://www.nuvopathsystems.example/
http://www.quordesk.example/
I have attached a word document that gives a menu system/page layout format that we would like for our website as well as branch office phone numbers. Our logo is also attached that you can use for your design purposes. We currently do not have copy produced for all of the pages outlined in the word document, but would get this done during the project with the selected designer.
We would like the website to be SEO friendly & fully responsive. We would prefer a Wordpress format, however, we are open to HTML formats as well.

```html
<!DOCTYPE html>
<html lang="en">
<head>
<meta charset="utf-8">
<title>Korvex IT — Commercial IT Support</title>
<link href="https://fonts.googleapis.com/css2?family=Exo:wght@300;400;600&family=Open+Sans:wght@400;600&display=swap" rel="stylesheet">
<style>
:root{
  --blue:#0b74c4;
  --blue-dark:#075a9c;
  --blue-light:#2a8fd9;
  --ink:#333;
  --muted:#666;
  --grey:#888;
  --footer:#1f1f1f;
  --footer-line:#3a3a3a;
  --white:#fff;
}
*{box-sizing:border-box;margin:0;padding:0}
html,body{width:1200px;height:3696px;overflow:hidden}
body{position:relative;font-family:"Open Sans",Arial,sans-serif;color:var(--ink);background:var(--white)}
.abs{position:absolute}
.heading{font-family:"Exo",Arial,sans-serif;font-weight:300}

/* Header / hero */
.hero{left:0;top:0;width:1200px;height:678px;background:linear-gradient(180deg,#c9d6e2 0%,#6f8aa3 18%,#2e4a66 45%,#14263a 100%)}
.brand{left:74px;top:22px;display:flex;align-items:center;gap:14px;color:var(--blue-dark);font-family:"Exo",Arial,sans-serif;font-weight:600;font-size:40px}
.brand-dot{width:46px;height:46px;border-radius:50%;background:var(--blue)}
.nav{right:70px;top:34px;display:flex;gap:10px;font-size:17px}
.nav a{color:#333;text-decoration:none;padding:9px 14px;border-radius:4px}
.nav a.active{background:var(--blue);color:var(--white)}
.hero-title{left:0;width:1200px;top:305px;text-align:center;color:var(--white);font-family:"Exo",Arial,sans-serif;font-weight:600;font-size:62px}
.hero-sub{left:0;width:1200px;top:382px;text-align:center;color:var(--white);font-size:20px;font-weight:600}
.btn{display:inline-block;font-family:"Exo",Arial,sans-serif;font-size:24px;letter-spacing:.5px;text-align:center;border-radius:5px}
.btn-solid{background:var(--blue);color:var(--white)}
.btn-ghost{border:2px solid var(--white);color:var(--white)}
.hero-btn{left:492px;top:430px;width:210px;height:54px;line-height:54px}

/* Welcome */
.welcome{left:0;top:678px;width:1200px;height:394px;background:var(--blue)}
.section-title{left:0;width:1200px;text-align:center;font-size:50px}
.welcome .section-title{top:50px;color:var(--white)}
.intro{left:150px;width:900px;text-align:center;font-size:13.5px;line-height:28px}
.welcome .intro{top:120px;color:var(--white)}
.welcome-btn{left:504px;top:274px;width:192px;height:58px;line-height:54px}

/* Why */
.why{left:0;top:1072px;width:1200px;height:628px;background:linear-gradient(100deg,#6c7784 0%,#a7b1bc 35%,#8a7c70 60%,#2f3a48 100%)}
.why-card{left:111px;top:66px;width:419px;height:500px;background:rgba(255,255,255,.82);padding:40px 26px}
.why-card h2{font-family:"Exo",Arial,sans-serif;font-weight:400;font-size:44px;color:var(--blue);margin-bottom:16px}
.why-card p{font-size:13.5px;line-height:27px;color:#222;margin-bottom:14px}
.why-btn{width:194px;height:56px;line-height:56px;margin-top:6px}

/* Services */
.services-head{left:0;top:1700px;width:1200px;height:394px}
.services-head .section-title{top:50px;color:var(--blue)}
.services-head .intro{top:120px;color:var(--muted)}
.tabs{left:390px;top:190px;width:420px;display:flex;justify-content:space-between}
.tab{width:120px;text-align:center;font-family:"Exo",Arial,sans-serif;font-size:22px;letter-spacing:1px;color:var(--grey)}
.tab svg{display:block;margin:0 auto 10px}
.tab.active{color:var(--blue)}
.divider{left:100px;top:2092px;width:1000px;height:2px;background:linear-gradient(90deg,transparent,#ddd 30%,#ddd 70%,transparent)}

.grid-item{width:240px;text-align:center;font-size:15px;color:#444;line-height:22px}
.grid-item .icon{width:136px;height:136px;margin:0 auto 16px;border-radius:50%;border:6px solid #e2e2e2;background:radial-gradient(circle,#5aa6de 0%,#2b6fa8 45%,#f1f1f1 46%,#d9d9d9 100%)}
.grid-item.featured{background:var(--blue);color:var(--white);height:185px;padding-top:28px}
.grid-item.featured .icon{width:130px;height:96px;border:0;border-radius:0;background:linear-gradient(135deg,#8fd0f2,#2a8fd9 60%,#f0a33a);margin-bottom:18px}

/* Contact */
.contact{left:0;top:2870px;width:1200px;height:500px;background:linear-gradient(135deg,#0b5ea3 0%,#1e86d2 45%,#0a64ad 100%)}
.contact .section-title{top:52px;color:var(--white);font-weight:400}
.contact .intro{top:114px;color:var(--white)}
.field{background:var(--white);border-radius:3px;font-size:13px;color:#999;padding:14px 12px}
.submit{left:517px;top:382px;width:163px;height:52px;line-height:48px}

/* Footer */
.footer{left:0;top:3370px;width:1200px;height:326px;background:var(--footer);color:#cfcfcf}
.foot-title{font-family:"Exo",Arial,sans-serif;font-size:21px;color:var(--blue-light);letter-spacing:1px}
.foot-list{list-style:none;font-size:16px}
.foot-list li{display:flex;align-items:center;gap:14px;height:42px}
.foot-brand{left:430px;top:40px;width:340px;display:flex;justify-content:center;align-items:center;gap:14px;font-family:"Exo",Arial,sans-serif;font-weight:600;font-size:42px;color:var(--white)}
.social{left:515px;top:176px;display:flex;gap:10px}
.social span{width:46px;height:46px;border-radius:50%;border:2px solid #555}
.social span.on{background:var(--blue);border-color:var(--blue)}
.foot-rule{left:75px;top:264px;width:1050px;height:1px;background:var(--footer-line)}
.copy{left:0;width:1200px;top:288px;text-align:center;font-size:13px}
</style>
</head>
<body>

<header class="abs hero" role="img" aria-label="Night city skyline with skyscrapers">
</header>
<div class="abs brand"><span class="brand-dot"></span>Korvex IT</div>
<nav class="abs nav">
  <a class="active" href="#">HOME</a><a href="#">ABOUT US</a><a href="#">SERVICES</a><a href="#">WHY KORVEX IT</a><a href="#">CONTACT</a>
</nav>
<h1 class="abs hero-title">Get More From Your Technology</h1>
<p class="abs hero-sub">Provides Commercial IT Support And Services To Small And Medium Sized Businesses</p>
<a class="abs btn btn-solid hero-btn">CONTACT US</a>

<section class="abs welcome">
  <h2 class="abs section-title heading">Welcome to Korvex IT</h2>
  <p class="abs intro">Lorem Ipsum is simply dummy text of the printing and typesetting industry. Lorem Ipsum has been the industry's standard dummy text ever since the 1500s, when an unknown printer took a galley of type and scrambled it to make a type specimen book. It has survived not only five centuries, but also the leap into electronic typesetting, remaining essentially unchanged. It was popularised in the 1960s with the release of transfer sheets containing Lorem Ipsum passages, and more recently with desktop publishing software like modern page editors including versions of Lorem Ipsum.</p>
  <a class="abs btn btn-ghost welcome-btn">KNOW MORE</a>
</section>

<section class="abs why" role="img" aria-label="Office photo of two colleagues working at a laptop">
  <div class="abs why-card">
    <h2>Why Korvex IT</h2>
    <p>Lorem Ipsum is simply dummy text of the printing and typesetting industry. Lorem Ipsum has been the industry's standard dummy text ever since the 1500s, when an unknown printer took a galley.</p>
    <p>Of type and scrambled it to make a type specimen book. It has survived not only five centuries, but also the leap into electronic typesetting, remaining essentially unchanged. It was popularised in the 1960s with the release of transfer sheets containing Lorem Ipsum passages.</p>
    <a class="btn btn-solid why-btn">KNOW MORE</a>
  </div>
</section>

<section class="abs services-head">
  <h2 class="abs section-title heading">Our Best Services</h2>
  <p class="abs intro">Lorem Ipsum is simply dummy text of the printing and typesetting industry. Lorem Ipsum has been the industry's standard dummy text ever since the 1500s, when an unknown printer took a</p>
  <div class="abs tabs">
    <div class="tab active">
      <svg width="96" height="96" viewBox="0 0 96 96"><g fill="#0b74c4"><ellipse cx="38" cy="18" rx="30" ry="10"/><path d="M8 24v14c0 6 14 10 30 10s30-4 30-10V24c0 6-14 10-30 10S8 30 8 24z"/><path d="M8 44v14c0 6 14 10 30 10V54C22 54 8 50 8 44z"/></g><circle cx="66" cy="66" r="22" fill="none" stroke="#0b74c4" stroke-width="7"/><path d="M82 48l6 14-14-2z" fill="#0b74c4"/></svg>
      DATA
      <svg width="24" height="14" viewBox="0 0 24 14" style="margin:8px auto 0"><path d="M0 0h24L12 14z" fill="#0b74c4"/></svg>
    </div>
    <div class="tab">
      <svg width="96" height="96" viewBox="0 0 96 96"><rect x="34" y="4" width="28" height="52" rx="14" fill="#888"/><path d="M24 44c0 14 10 24 24 24s24-10 24-24" fill="none" stroke="#888" stroke-width="5"/><rect x="45" y="68" width="6" height="18" fill="#888"/><rect x="32" y="86" width="32" height="6" fill="#888"/></svg>
      CLOUD
    </div>
    <div class="tab">
      <svg width="96" height="96" viewBox="0 0 96 96"><path d="M20 60a16 16 0 0 1 6-30 22 22 0 0 1 42 4 14 14 0 0 1 4 26z" fill="#999"/><rect x="10" y="66" width="76" height="14" rx="4" fill="#999"/></svg>
      VOICE
    </div>
  </div>
</section>
<div class="abs divider"></div>

<div class="abs grid-item featured" style="left:76px;top:2163px"><div class="icon" role="img" aria-label="Managed services illustration"></div>MANAGED IT SERVICES</div>
<div class="abs grid-item" style="left:348px;top:2160px"><div class="icon" role="img" aria-label="Support consultant illustration"></div>IT SUPPORT &amp; CONSULTING</div>
<div class="abs grid-item" style="left:609px;top:2160px"><div class="icon" role="img" aria-label="Helpdesk operator illustration"></div>IT HELPDESK SERVICES</div>
<div class="abs grid-item" style="left:878px;top:2160px"><div class="icon" role="img" aria-label="Network security illustration"></div>NETWORK SECURITY</div>

<div class="abs grid-item" style="left:77px;top:2380px"><div class="icon" role="img" aria-label="Data backup illustration"></div>DATA BACKUP &amp; RECOVERY</div>
<div class="abs grid-item" style="left:348px;top:2380px"><div class="icon" role="img" aria-label="Cloud servers illustration"></div>SERVERS &amp; VIRTUALIZATION</div>
<div class="abs grid-item" style="left:609px;top:2380px"><div class="icon" role="img" aria-label="Network cabling illustration"></div>STRUCTURED CABLING</div>
<div class="abs grid-item" style="left:878px;top:2380px"><div class="icon" role="img" aria-label="Wireless router illustration"></div>WIRELESS NETWORKING</div>

<div class="abs grid-item" style="left:348px;top:2606px"><div class="icon" role="img" aria-label="Email threat shield illustration"></div>EMAIL &amp; SPAM THREAT<br>MANAGEMENT</div>
<div class="abs grid-item" style="left:609px;top:2606px"><div class="icon" role="img" aria-label="Remote monitoring illustration"></div>REMOTE MONITORING<br>SERVICES</div>

<section class="abs contact" role="img" aria-label="Blue technology background with hexagons and world map">
  <h2 class="abs section-title heading">Contact Us</h2>
  <p class="abs intro">Lorem Ipsum is simply dummy text of the printing and typesetting industry. Lorem Ipsum has been the industry's standard dummy text ever since the 1500s, when an unknown printer took a</p>
  <div class="abs field" style="left:150px;top:193px;width:294px;height:50px">Name*</div>
  <div class="abs field" style="left:453px;top:193px;width:291px;height:50px">Email*</div>
  <div class="abs field" style="left:754px;top:193px;width:293px;height:50px">Phone*</div>
  <div class="abs field" style="left:150px;top:254px;width:897px;height:112px">Message*</div>
  <a class="abs btn btn-ghost submit">SUBMIT</a>
</section>

<footer class="abs footer">
  <div class="abs foot-title" style="left:79px;top:40px">CONTACT US</div>
  <ul class="abs foot-list" style="left:79px;top:88px">
    <li><svg width="22" height="22" viewBox="0 0 24 24"><path d="M6.6 10.8a15 15 0 0 0 6.6 6.6l2.2-2.2a1 1 0 0 1 1-.25 11.4 11.4 0 0 0 3.6.57 1 1 0 0 1 1 1V20a1 1 0 0 1-1 1A17 17 0 0 1 3 4a1 1 0 0 1 1-1h3.5a1 1 0 0 1 1 1c0 1.25.2 2.45.57 3.57a1 1 0 0 1-.25 1z" fill="#2a8fd9"/></svg>Main Number : 972-555-0140</li>
    <li><svg width="22" height="22" viewBox="0 0 24 24"><path d="M6.6 10.8a15 15 0 0 0 6.6 6.6l2.2-2.2a1 1 0 0 1 1-.25 11.4 11.4 0 0 0 3.6.57 1 1 0 0 1 1 1V20a1 1 0 0 1-1 1A17 17 0 0 1 3 4a1 1 0 0 1 1-1h3.5a1 1 0 0 1 1 1c0 1.25.2 2.45.57 3.57a1 1 0 0 1-.25 1z" fill="#2a8fd9"/></svg>Houston: 832-555-0172</li>
    <li><svg width="22" height="22" viewBox="0 0 24 24"><path d="M6.6 10.8a15 15 0 0 0 6.6 6.6l2.2-2.2a1 1 0 0 1 1-.25 11.4 11.4 0 0 0 3.6.57 1 1 0 0 1 1 1V20a1 1 0 0 1-1 1A17 17 0 0 1 3 4a1 1 0 0 1 1-1h3.5a1 1 0 0 1 1 1c0 1.25.2 2.45.57 3.57a1 1 0 0 1-.25 1z" fill="#2a8fd9"/></svg>San Antonio : 210-555-0136</li>
  </ul>
  <div class="abs foot-brand"><span class="brand-dot"></span>Korvex IT</div>
  <div class="abs social"><span class="on"></span><span></span><span></span></div>
  <div class="abs foot-title" style="left:788px;top:40px">CONTACT US</div>
  <ul class="abs foot-list" style="left:788px;top:88px">
    <li><svg width="22" height="22" viewBox="0 0 24 24"><path d="M6.6 10.8a15 15 0 0 0 6.6 6.6l2.2-2.2a1 1 0 0 1 1-.25 11.4 11.4 0 0 0 3.6.57 1 1 0 0 1 1 1V20a1 1 0 0 1-1 1A17 17 0 0 1 3 4a1 1 0 0 1 1-1h3.5a1 1 0 0 1 1 1c0 1.25.2 2.45.57 3.57a1 1 0 0 1-.25 1z" fill="#2a8fd9"/></svg>Austin : 512-555-0118</li>
    <li><svg width="22" height="22" viewBox="0 0 24 24"><path d="M6.6 10.8a15 15 0 0 0 6.6 6.6l2.2-2.2a1 1 0 0 1 1-.25 11.4 11.4 0 0 0 3.6.57 1 1 0 0 1 1 1V20a1 1 0 0 1-1 1A17 17 0 0 1 3 4a1 1 0 0 1 1-1h3.5a1 1 0 0 1 1 1c0 1.25.2 2.45.57 3.57a1 1 0 0 1-.25 1z" fill="#2a8fd9"/></svg>Tulsa : 918-555-0164</li>
    <li><svg width="22" height="22" viewBox="0 0 24 24"><path d="M6.6 10.8a15 15 0 0 0 6.6 6.6l2.2-2.2a1 1 0 0 1 1-.25 11.4 11.4 0 0 0 3.6.57 1 1 0 0 1 1 1V20a1 1 0 0 1-1 1A17 17 0 0 1 3 4a1 1 0 0 1 1-1h3.5a1 1 0 0 1 1 1c0 1.25.2 2.45.57 3.57a1 1 0 0 1-.25 1z" fill="#2a8fd9"/></svg>Oklahoma City : 405-555-0107</li>
  </ul>
  <div class="abs foot-rule"></div>
  <p class="abs copy">©Korvex IT- 2017 All Right Reserved</p>
</footer>

</body>
</html>
```